Business Card Design Project

Use our current logo. Clean design.

Industry/Entity Type

Business

Requirements
Must have
• Marisela DUBRANCQ
M. Law
Managing Partner

Alpenvorsa AG
Kornhalmweg 214
CH-3097 Liebefeld

M. +41 79 412 56 27
T. +41 31 928 44 10
F. +41 31 928 44 19

m.dubrancq@alpenvorsa-example.com
www.alpenvorsa-example.com

```html
<!DOCTYPE html>
<html lang="en">
<head>
<meta charset="utf-8">
<title>Alpenvorsa AG – Business Card Variants</title>
<link rel="stylesheet" href="https://fonts.googleapis.com/css2?family=Bebas+Neue&display=swap">
<style>
  :root {
    --brand-red: #c0140f;
    --ink: #141414;
    --card-paper: #f1f2f3;
    --divider-grey: #9ba3a4;
    --logo-white: #fafafa;
  }
  * { margin: 0; padding: 0; box-sizing: border-box; }
  html, body {
    width: 1200px; height: 690px; overflow: hidden;
    background: var(--divider-grey);
  }
  .sheet { position: relative; width: 1200px; height: 690px; }
  .card {
    position: absolute; width: 595px; height: 340px;
    background: var(--card-paper);
    font-family: "Bebas Neue", "Oswald", sans-serif;
    color: var(--ink);
    overflow: hidden;
  }
  .card--a { left: 0; top: 0; }
  .card--b { left: 605px; top: 0; }
  .card--c { left: 0; top: 349px; height: 341px; }
  .card--d { left: 605px; top: 349px; height: 341px; }

  .logo-tile {
    position: absolute; left: 16px; top: 0;
    width: 152px; height: 153px;
    border-radius: 0 0 5px 5px;
    display: flex; align-items: center; justify-content: center;
  }
  .logo-tile--red { background: var(--brand-red); }
  .logo-tile--white {
    background: var(--logo-white);
    box-shadow: 0 2px 4px rgba(0,0,0,.25);
  }
  .logo-name {
    font-size: 30px; letter-spacing: 1px; line-height: 1;
  }
  .logo-tile--red .logo-name { color: #ffffff; }
  .logo-tile--white .logo-name { color: var(--ink); }

  .holder-name {
    position: absolute; left: 178px;
    white-space: nowrap; line-height: 1;
  }
  .holder-name--large { font-size: 46px; top: 50px; }
  .card--d .holder-name--large { top: 56px; }
  .holder-name--stacked { font-size: 37px; top: 20px; color: var(--brand-red); }

  .holder-role { position: absolute; left: 178px; top: 60px; font-size: 27px; line-height: 34px; }

  .degree { position: absolute; left: 30px; top: 185px; line-height: 1; }
  .degree__title { font-size: 44px; color: var(--brand-red); display: block; }
  .degree__role { font-size: 17px; display: block; margin-top: 2px; }

  .address-block {
    position: absolute; left: 30px; font-size: 18px; line-height: 22.5px;
  }
  .card--b .address-block { top: 210px; }
  .card--c .address-block { top: 220px; }

  .label { color: var(--brand-red); }

  .contact-list { position: absolute; list-style: none; white-space: nowrap; }
  .contact-list--compact { left: 351px; top: 137px; font-size: 14px; line-height: 22px; }
  .card--d .contact-list--compact { top: 140px; }
  .contact-list--roomy { left: 340px; font-size: 16.5px; line-height: 25px; }
  .card--b .contact-list--roomy { top: 186px; }
  .card--c .contact-list--roomy { top: 188px; }

  .accent-bar {
    position: absolute; left: 351px; right: 0; bottom: 0; height: 17px;
    background: var(--brand-red);
  }
</style>
</head>
<body>
<main class="sheet">

  <!-- Variant A: red logo tile, large name -->
  <section class="card card--a">
    <div class="logo-tile logo-tile--red"><span class="logo-name">Alpenvorsa</span></div>
    <h1 class="holder-name holder-name--large">Marisela Dubrancq</h1>
    <p class="degree"><span class="degree__title">M. Law</span><span class="degree__role">Managing Partner</span></p>
    <ul class="contact-list contact-list--compact">
      <li><span class="label">Address:</span> Alpenvorsa AG</li>
      <li>Kornhalmweg 214</li>
      <li>CH-3097 Liebefeld</li>
      <li><span class="label">Mobile:</span> +41 79 412 56 27</li>
      <li><span class="label">Phone:</span> +41 31 928 44 10</li>
      <li><span class="label">Fax:</span> +41 31 928 44 19</li>
      <li><span class="label">Email:</span> m.dubrancq@alpenvorsa-example.com</li>
      <li><span class="label">Web:</span> www.alpenvorsa-example.com</li>
    </ul>
    <div class="accent-bar"></div>
  </section>

  <!-- Variant B: red logo tile, stacked title -->
  <section class="card card--b">
    <div class="logo-tile logo-tile--red"><span class="logo-name">Alpenvorsa</span></div>
    <h1 class="holder-name holder-name--stacked">Marisela Dubrancq</h1>
    <p class="holder-role">M. Law<br>Managing Partner</p>
    <p class="address-block"><span class="label">Address</span><br>Alpenvorsa AG<br>Kornhalmweg 214<br>CH-3097 Liebefeld</p>
    <ul class="contact-list contact-list--roomy">
      <li><span class="label">Mobile:</span> +41 79 412 56 27</li>
      <li><span class="label">Phone:</span> +41 31 928 44 10</li>
      <li><span class="label">Fax:</span> +41 31 928 44 19</li>
      <li><span class="label">Email:</span> m.dubrancq@alpenvorsa-example.com</li>
      <li><span class="label">Web:</span> www.alpenvorsa-example.com</li>
    </ul>
    <div class="accent-bar"></div>
  </section>

  <!-- Variant C: white logo tile, stacked title -->
  <section class="card card--c">
    <div class="logo-tile logo-tile--white"><span class="logo-name">Alpenvorsa</span></div>
    <h1 class="holder-name holder-name--stacked">Marisela Dubrancq</h1>
    <p class="holder-role">M. Law<br>Managing Partner</p>
    <p class="address-block"><span class="label">Address</span><br>Alpenvorsa AG<br>Kornhalmweg 214<br>CH-3097 Liebefeld</p>
    <ul class="contact-list contact-list--roomy">
      <li><span class="label">Mobile:</span> +41 79 412 56 27</li>
      <li><span class="label">Phone:</span> +41 31 928 44 10</li>
      <li><span class="label">Fax:</span> +41 31 928 44 19</li>
      <li><span class="label">Email:</span> m.dubrancq@alpenvorsa-example.com</li>
      <li><span class="label">Web:</span> www.alpenvorsa-example.com</li>
    </ul>
    <div class="accent-bar"></div>
  </section>

  <!-- Variant D: white logo tile, large name -->
  <section class="card card--d">
    <div class="logo-tile logo-tile--white"><span class="logo-name">Alpenvorsa</span></div>
    <h1 class="holder-name holder-name--large">Marisela Dubrancq</h1>
    <p class="degree"><span class="degree__title">M. Law</span><span class="degree__role">Managing Partner</span></p>
    <ul class="contact-list contact-list--compact">
      <li><span class="label">Address:</span> Alpenvorsa AG</li>
      <li>Kornhalmweg 214</li>
      <li>CH-3097 Liebefeld</li>
      <li><span class="label">Mobile:</span> +41 79 412 56 27</li>
      <li><span class="label">Phone:</span> +41 31 928 44 10</li>
      <li><span class="label">Fax:</span> +41 31 928 44 19</li>
      <li><span class="label">Email:</span> m.dubrancq@alpenvorsa-example.com</li>
      <li><span class="label">Web:</span> www.alpenvorsa-example.com</li>
    </ul>
    <div class="accent-bar"></div>
  </section>

</main>
</body>
</html>
```